Solar company mail box flyer design

We are a solar installation company and we currently need a DL flyer design for mailbox distribution. The front page need to mention that the government rebate is going to be reduced from the first day of the next year. Also, it need to mentioned that $100 discount available for any customer who show us this flyer. We will also need to have some solar panels and inverters demonstrated on the front page.

I have attached some similar flyers for reference purpose.

```html
<!DOCTYPE html>
<html lang="en">
<head>
<meta charset="UTF-8">
<title>Solar DL Flyer</title>
<link rel="stylesheet" href="https://fonts.googleapis.com/css2?family=Bebas+Neue&family=Oswald:wght@500;600;700&family=Lato:wght@400;700;900&display=swap">
<style>
  :root {
    --stage: #3d3d3d;
    --blue: #1a6bb0;
    --blue-light: #2b93da;
    --blue-deep: #0f5a9f;
    --orange: #ef7622;
    --ink: #1b1b1b;
    --grey: #666666;
    --white: #ffffff;
  }
  * { box-sizing: border-box; margin: 0; padding: 0; }
  html, body { width: 1200px; height: 1200px; overflow: hidden; }
  body { background: var(--stage); position: relative; font-family: "Lato", sans-serif; }

  .panel {
    position: absolute; top: 98px; width: 492px; height: 1010px;
    background: var(--white); overflow: hidden;
    box-shadow: 0 6px 18px rgba(0,0,0,.45);
  }
  .panel--front { left: 86px; }
  .panel--back { left: 625px; }
  .panel svg.backdrop { position: absolute; inset: 0; width: 492px; height: 1010px; }

  /* Front */
  .brand-name {
    position: absolute; top: 26px; left: 0; width: 100%; text-align: center;
    font-family: "Oswald", sans-serif; font-weight: 600; font-size: 40px; letter-spacing: .5px;
    color: var(--blue);
  }
  .brand-name .accent { color: var(--orange); }
  .product-circle {
    position: absolute; left: 130px; top: 418px; width: 232px; height: 232px; border-radius: 50%;
    border: 8px solid var(--orange);
    background: radial-gradient(circle at 50% 45%, #ffffff 0%, #f1f2f4 45%, #c9ccd6 70%, #8f9bb8 100%);
  }
  .headline {
    position: absolute; top: 658px; left: 0; width: 100%; text-align: center;
    color: var(--blue);
  }
  .headline__caps { font-family: "Bebas Neue", sans-serif; font-size: 48px; line-height: 47px; display: block; }
  .headline__sub {
    display: block; font-family: "Oswald", sans-serif; font-weight: 600; font-size: 33px; line-height: 44px;
    color: var(--orange);
  }
  .offer {
    position: absolute; top: 814px; left: 0; width: 100%; height: 90px;
    background: linear-gradient(180deg, var(--blue-light), var(--blue-deep));
    padding: 7px 16px;
  }
  .offer__frame {
    height: 76px; border: 2px dashed rgba(255,255,255,.85); text-align: center; color: var(--white);
    padding-top: 4px;
  }
  .offer__title { font-weight: 700; font-size: 30px; line-height: 36px; }
  .offer__note { font-size: 21px; line-height: 26px; }
  .callout {
    position: absolute; top: 926px; left: 0; width: 100%; text-align: center;
    font-weight: 700; font-size: 34px; color: var(--ink);
  }
  .front-footer { position: absolute; bottom: 0; left: 0; width: 100%; height: 27px; background: var(--orange); }

  /* Back */
  .pill {
    position: absolute; height: 43px; border-radius: 22px;
    background: linear-gradient(180deg, var(--blue-light), var(--blue-deep));
    color: var(--white); text-align: center;
    font-family: "Oswald", sans-serif; font-weight: 600; font-size: 29px; line-height: 43px;
    box-shadow: 0 5px 4px -3px rgba(0,0,0,.35);
  }
  .pill--about { left: 153px; top: 26px; width: 185px; }
  .pill--why { left: 124px; top: 359px; width: 244px; }
  .pill--services { left: 135px; top: 600px; width: 222px; }

  .about { position: absolute; left: 34px; top: 82px; width: 428px; font-size: 14px; line-height: 17.8px; color: var(--ink); }
  .about p { text-align: justify; text-align-last: center; margin-bottom: 8px; }

  .reasons { position: absolute; left: 36px; top: 414px; width: 428px; list-style: none; font-size: 14px; line-height: 17.8px; color: var(--ink); }
  .reasons li { position: relative; padding-left: 31px; margin-bottom: 8.6px; text-align: justify; }
  .reasons svg { position: absolute; left: 0; top: 1px; width: 17px; height: 15px; }

  .services { position: absolute; left: 49px; top: 658px; list-style: none; font-size: 15px; font-weight: 700; line-height: 26.4px; color: var(--ink); }
  .services li { position: relative; padding-left: 18px; }
  .services li::before {
    content: ""; position: absolute; left: 0; top: 8px; width: 10px; height: 10px; border-radius: 50%; background: var(--orange);
  }
  .brand-stack {
    position: absolute; left: 44px; top: 784px;
    font-family: "Oswald", sans-serif; font-weight: 600; font-size: 34px; line-height: 38px; color: var(--blue);
  }
  .brand-stack .accent { color: var(--orange); }
  .product-card {
    position: absolute; left: 266px; top: 730px; width: 200px; height: 260px; border-radius: 34px;
    background: linear-gradient(160deg, #ffffff 0%, #f3f4f6 60%, #d7d9dd 100%);
    box-shadow: 4px 6px 10px rgba(0,0,0,.25);
  }
  .website {
    position: absolute; left: 46px; top: 958px; font-weight: 700; font-size: 16px; color: var(--white);
  }
</style>
</head>
<body>

<section class="panel panel--front">
  <svg class="backdrop" viewBox="0 0 492 1010" aria-hidden="false">
    <defs>
      <linearGradient id="sunsetPanels" x1="0" y1="0" x2="0" y2="1">
        <stop offset="0" stop-color="#ffffff"/>
        <stop offset=".16" stop-color="#f3f2f4"/>
        <stop offset=".24" stop-color="#c8c3c8"/>
        <stop offset=".3" stop-color="#f5a44c"/>
        <stop offset=".33" stop-color="#e46a20"/>
        <stop offset=".37" stop-color="#6d7189"/>
        <stop offset=".55" stop-color="#405b87"/>
        <stop offset="1" stop-color="#1f3158"/>
      </linearGradient>
    </defs>
    <rect x="0" y="0" width="492" height="560" fill="url(#sunsetPanels)" role="img" aria-label="Photo of rooftop solar panels at sunset"/>
    <path d="M0 490 C120 505 200 520 246 520 C330 520 420 485 492 470 L492 505 C420 525 330 560 246 565 C180 565 100 530 0 505 Z" fill="#1a74c0"/>
    <path d="M0 505 C100 530 180 565 246 565 C330 560 420 525 492 505 L492 582 C420 585 330 600 246 600 C180 600 80 560 0 545 Z" fill="#ef7622"/>
    <path d="M0 545 C80 560 180 600 246 600 C330 600 420 585 492 582 L492 1010 L0 1010 Z" fill="#ffffff"/>
  </svg>

  <h1 class="brand-name">COMPANY <span class="accent">LOGO</span></h1>

  <div class="product-circle" role="img" aria-label="Photo of three solar inverters in blue, red and white"></div>

  <h2 class="headline">
    <span class="headline__caps">Government rebate is going<br>to be reduced from</span>
    <span class="headline__sub">the first day of the Next Year</span>
  </h2>

  <div class="offer">
    <div class="offer__frame">
      <p class="offer__title">$100 DISCOUNT AVAILABLE</p>
      <p class="offer__note">for any customer who show us this flyer.</p>
    </div>
  </div>

  <p class="callout">Call us @ 12345678900</p>
  <div class="front-footer"></div>
</section>

<section class="panel panel--back">
  <svg class="backdrop" viewBox="0 0 492 1010" aria-hidden="true">
    <path d="M0 935 C140 865 320 830 492 836 L492 868 C320 860 150 895 0 955 Z" fill="#1a74c0"/>
    <path d="M0 955 C150 895 320 860 492 868 L492 945 C330 905 160 925 0 968 Z" fill="#ef7622"/>
    <path d="M0 968 C160 925 330 905 492 945 L492 1010 L0 1010 Z" fill="#666666"/>
  </svg>

  <h2 class="pill pill--about">ABOUT US</h2>
  <div class="about">
    <p>Lorem ipsum dolor sit amet, consectetur adipiscing elsmod tempor incididunt ut labore et dolore magna aliqua. Orci eu lobortis elntum nibh. Pellentesque nec nam aliquam sem. Sagittis purus sit amet vlutpat consequat mauris nunc. Porttitor rhoncus dolor purus non. Enim tortor at auctor urna. Pharetra sit ametquam id diam maecnas. Cras pulvinar mattis nunc sed blandit lutpat sed. Vel elit scelerisque mauris pellentesque pulvinar pellentesque.</p>
    <p>Hac habitasse platea dictumst quisque sagittis purus sit amet. Amet cursus sit amet dictum. Lacus suspendisse faucibus interdum posuere lorem. Fames ac turpis egestas sed tempus urna et. In vitae turpis massa sed elementum tempus egestas sed sed. Venenatis urna cursus eget nunc scelerisque viverra mauris. Sollicitudin aliquam ultrices sagittis orci a scelerisque purus. Diam sollicitudin tempor id eu nisl nunc mi ipsum.</p>
  </div>

  <h2 class="pill pill--why">WHY CHOOSE US</h2>
  <ul class="reasons">
    <li><svg viewBox="0 0 17 15"><rect x="1" y="3" width="11" height="11" fill="none" stroke="#ef7622" stroke-width="1.6"/><path d="M3.5 8 L7 11.5 L16 1.5" fill="none" stroke="#ef7622" stroke-width="2.2"/></svg>Lorem ipsum dolor sit amet, consectetur adipiscing elsmod tempor incididunt ut labore et dolore magna aliqua.</li>
    <li><svg viewBox="0 0 17 15"><rect x="1" y="3" width="11" height="11" fill="none" stroke="#ef7622" stroke-width="1.6"/><path d="M3.5 8 L7 11.5 L16 1.5" fill="none" stroke="#ef7622" stroke-width="2.2"/></svg>Orci eu lobortis elntum nibh.</li>
    <li><svg viewBox="0 0 17 15"><rect x="1" y="3" width="11" height="11" fill="none" stroke="#ef7622" stroke-width="1.6"/><path d="M3.5 8 L7 11.5 L16 1.5" fill="none" stroke="#ef7622" stroke-width="2.2"/></svg>Pellentesque nec nam aliquam sem.</li>
    <li><svg viewBox="0 0 17 15"><rect x="1" y="3" width="11" height="11" fill="none" stroke="#ef7622" stroke-width="1.6"/><path d="M3.5 8 L7 11.5 L16 1.5" fill="none" stroke="#ef7622" stroke-width="2.2"/></svg>Sagittis purus sit amet vlutpat consequat mauris nunc.</li>
    <li><svg viewBox="0 0 17 15"><rect x="1" y="3" width="11" height="11" fill="none" stroke="#ef7622" stroke-width="1.6"/><path d="M3.5 8 L7 11.5 L16 1.5" fill="none" stroke="#ef7622" stroke-width="2.2"/></svg>Porttitor rhoncus dolor purus non. Enim tortor at auctor</li>
    <li><svg viewBox="0 0 17 15"><rect x="1" y="3" width="11" height="11" fill="none" stroke="#ef7622" stroke-width="1.6"/><path d="M3.5 8 L7 11.5 L16 1.5" fill="none" stroke="#ef7622" stroke-width="2.2"/></svg>Pharetra sit ametquam id diam maecnas.</li>
  </ul>

  <h2 class="pill pill--services">OUR SERVICES</h2>
  <ul class="services">
    <li>Lorem ipsum dolor sit amet, consectetur adipiscing</li>
    <li>Orci eu lobortis elntum nibh.</li>
    <li>Pellentesque nec nam</li>
    <li>Amet vlutpat</li>
  </ul>

  <div class="brand-stack">COMPANY<br><span class="accent">LOGO</span></div>

  <div class="product-card" role="img" aria-label="Photo of a white wall-mounted solar inverter"></div>

  <p class="website">www.companyname.com</p>
</section>

</body>
</html>
```